KTR Engineering Business Card Design

We’re looking for an elegant, clean, and timeless business card design that communicates experience, capability, and reliability.

KTR Engineering was established in 1995 , we are a Government Contracting company providing Professional Services to the Ministry of Harbor Works, Frontier Stewardship and the Waypoint Consortium. Our capabilities include: Acquisition & Program Management; Intelligence & Security Operations; Cyber, IT & Network Operations; Lifecycle Logistics & Asset Readiness; C5ISR Systems Engineering & Sustainment.

We want the card to reflect a straightforward, confident approach to business. The design should feel polished and professional without being flashy or overly corporate.

Design Direction
Clean, sophisticated, and uncluttered
Elegant but understated
Strong typography and thoughtful spacing
A timeless aesthetic rather than something overly trendy
Confident and established, with a sense of substance
Easy to read and practical in a real-world business setting

The overall impression should be: “These are experienced professionals who know what they’re doing, do what they say, and can be relied upon.”

We’re open to creative interpretations. The finished card should feel distinctive through its typography, proportions, layout, and attention to detail rather than through excessive graphics or visual effects.

We’re looking for a design that would make a potential client immediately feel that they’re dealing with a capable, trustworthy, and established company.

Company Colors: Navy and Gold/Yellow (but you do not need to use these colors on the card)
Company Name: KTR Engineering Associates, Inc. (known as KTR Engineering)
Website: ktrengineering.example
Company Logo: Navy & Gold (other variations attached)

```html
<!DOCTYPE html>
<html lang="en">
<head>
<meta charset="UTF-8">
<title>KTR Engineering Business Card</title>
<link rel="stylesheet" href="https://fonts.googleapis.com/css2?family=Archivo:wght@600&family=Poppins:wght@400;700&display=swap">
<style>
  :root {
    --stage: #8a8a8c;
    --navy-deep: #1f2656;
    --navy: #2a3266;
    --navy-light: #4a5a90;
    --haze: #67668c;
    --gold: #f5dc3c;
    --white: #ffffff;
  }
  * { margin: 0; padding: 0; box-sizing: border-box; }
  html, body { width: 900px; height: 1200px; overflow: hidden; }
  body {
    background: var(--stage);
    font-family: "Poppins", sans-serif;
    color: var(--white);
    position: relative;
  }
  .card {
    position: absolute;
    left: 136px;
    width: 630px;
    height: 363px;
    overflow: hidden;
  }
  .card-front {
    top: 214px;
    background: linear-gradient(135deg, var(--navy-deep), var(--navy) 70%, #2e3570);
    display: flex;
    align-items: center;
    justify-content: center;
  }
  .wordmark {
    font-family: "Poppins", sans-serif;
    font-weight: 700;
    color: var(--white);
    line-height: 1;
    letter-spacing: -2px;
  }
  .card-front .wordmark { font-size: 92px; }
  .card-back {
    top: 629px;
    background: linear-gradient(90deg, var(--navy-deep) 0%, var(--navy) 45%, var(--navy-light) 100%);
  }
  .aircraft-photo {
    position: absolute;
    right: 0; top: 0;
    width: 360px; height: 100%;
    background:
      radial-gradient(ellipse at 80% 100%, var(--haze) 0%, rgba(103,102,140,0) 60%),
      linear-gradient(90deg, rgba(74,90,144,0) 0%, rgba(74,90,144,0.55) 40%, rgba(78,92,140,0.9) 100%);
  }
  .card-back .wordmark {
    position: absolute;
    left: 366px;
    top: 160px;
    font-size: 92px;
  }
  .contact {
    position: absolute;
    left: 42px;
    top: 50px;
  }
  .person-name {
    font-family: "Archivo", sans-serif;
    font-weight: 600;
    font-size: 24px;
    letter-spacing: 0.2px;
  }
  .person-title {
    font-size: 16.5px;
    letter-spacing: 0.6px;
    margin-top: 2px;
  }
  .rule {
    width: 148px;
    height: 1.5px;
    background: var(--gold);
  }
  .rule.first { margin-top: 10px; }
  .address {
    font-size: 16px;
    line-height: 25px;
    letter-spacing: 0.6px;
    margin-top: 12px;
    margin-bottom: 8px;
  }
  .links { list-style: none; margin-top: 12px; }
  .links li {
    display: flex;
    align-items: center;
    gap: 8px;
    font-size: 16.5px;
    letter-spacing: 1px;
    height: 29px;
  }
  .links li.phone { letter-spacing: 2.4px; }
  .links svg { width: 13px; height: 13px; flex: none; }
</style>
</head>
<body>
  <section class="card card-front">
    <div class="wordmark">KTR</div>
  </section>

  <section class="card card-back">
    <div class="aircraft-photo" role="img" aria-label="Photograph of a fighter jet in flight against a hazy blue sky"></div>
    <div class="wordmark">KTR</div>
    <div class="contact">
      <h1 class="person-name">Marian Holloway, P.E.</h1>
      <p class="person-title">CEO &amp; President</p>
      <div class="rule first"></div>
      <p class="address">4120 Larkspur Avenue,<br>Suite 310, Port Halden,<br>ST 00000</p>
      <div class="rule"></div>
      <ul class="links">
        <li class="phone">
          <svg viewBox="0 0 24 24"><path fill="#f5dc3c" d="M6.6 10.8a15.1 15.1 0 0 0 6.6 6.6l2.2-2.2c.3-.3.7-.4 1-.2 1.1.4 2.3.6 3.6.6.6 0 1 .4 1 1V20c0 .6-.4 1-1 1A17 17 0 0 1 3 4c0-.6.4-1 1-1h3.5c.6 0 1 .4 1 1 0 1.3.2 2.5.6 3.6.1.3 0 .7-.2 1z"/></svg>
          555-010-4827
        </li>
        <li>
          <svg viewBox="0 0 24 24" fill="none" stroke="#f5dc3c" stroke-width="2.2"><circle cx="12" cy="12" r="9.5"/><ellipse cx="12" cy="12" rx="4" ry="9.5"/><path d="M2.5 12h19M4 7h16M4 17h16"/></svg>
          ktrengineering.example
        </li>
        <li>
          <svg viewBox="0 0 24 24"><circle cx="12" cy="12" r="11" fill="#f5dc3c"/></svg>
          ktr-engineering-associates-inc
        </li>
      </ul>
    </div>
  </section>
</body>
</html>
```